BOLD & MINIMALIST DESIGN NEEDED

We want a very bold but minimalistic business card design that is impactful and utilizes both sides of the business card. Our current logo is included for your use.

We want bold fonts and good use of negative space. We don't want the logo to overpower the design.

Target Market(s)

Professionals who are building new commercial buildings.

Industry/Entity Type

Construction

Contact Information for Business Card

Name, Title, email, office phone, cell phone, website

Font styles to use
Serif
Sans Serif

Requirements
Must have
• Bold design!

```html
<!DOCTYPE html>
<html lang="en">
<head>
<meta charset="utf-8">
<title>Ridgeline Design + Build — Business Card</title>
<link rel="stylesheet" href="https://fonts.googleapis.com/css2?family=Raleway:wght@500;700;800&family=Lato:wght@400;700&display=swap">
<style>
  :root {
    --stage: #2b2b2b;
    --green-light: #6fa225;
    --green-mid: #4d7c17;
    --green-dark: #2c4f0d;
    --accent: #5c9a1b;
    --ink: #151515;
    --grey: #4a4a4a;
    --paper: #ffffff;
    --shadow-block: #0d0d0d;
  }
  * { box-sizing: border-box; margin: 0; padding: 0; }
  html, body { width: 1200px; height: 800px; overflow: hidden; }
  body {
    background: var(--stage);
    font-family: "Lato", Arial, sans-serif;
    position: relative;
  }
  .card {
    position: absolute;
    width: 540px;
    height: 310px;
    border-radius: 18px;
    overflow: hidden;
    box-shadow: 0 14px 30px rgba(0,0,0,.45);
  }
  /* Front side */
  .card-front {
    left: 70px; top: 80px;
    background: radial-gradient(circle at 40% 40%, var(--green-light) 0%, var(--green-mid) 45%, var(--green-dark) 100%);
  }
  .front-brand {
    position: absolute;
    left: 44px; top: 118px;
    display: flex; align-items: center; gap: 12px;
  }
  .brand-square {
    width: 26px; height: 26px;
    background: var(--paper);
  }
  .brand-name {
    font-family: "Raleway", Arial, sans-serif;
    font-weight: 800;
    font-size: 36px;
    letter-spacing: 1px;
    line-height: 1;
    color: var(--paper);
  }
  .front-brand-sub {
    position: absolute;
    left: 82px; top: 162px;
    font-family: "Raleway", Arial, sans-serif;
    font-weight: 800;
    font-size: 13px;
    letter-spacing: 5px;
    color: var(--paper);
  }
  .front-symbol-area {
    position: absolute;
    right: 0; top: 0;
    width: 250px; height: 310px;
    background: linear-gradient(135deg, var(--shadow-block) 0%, #1d2a10 45%, var(--green-light) 100%);
  }
  /* Back side */
  .card-back {
    left: 590px; top: 410px;
    background: var(--paper);
  }
  .back-brand {
    position: absolute;
    left: 34px; top: 60px;
    display: flex; align-items: center; gap: 10px;
  }
  .back-brand .brand-square { background: var(--accent); width: 22px; height: 22px; }
  .back-brand .brand-name { color: var(--ink); font-size: 30px; }
  .back-brand-sub {
    position: absolute;
    left: 66px; top: 98px;
    font-family: "Raleway", Arial, sans-serif;
    font-weight: 800;
    font-size: 11px;
    letter-spacing: 4px;
    color: var(--ink);
  }
  .person {
    position: absolute;
    right: 34px; top: 44px;
    text-align: right;
  }
  .person-name {
    font-family: "Raleway", Arial, sans-serif;
    font-weight: 700;
    font-size: 30px;
    color: var(--accent);
  }
  .person-title {
    font-size: 15px;
    color: var(--grey);
    margin-top: 2px;
  }
  .rule {
    position: absolute;
    left: 34px; right: 34px; top: 150px;
    height: 1.5px;
    background: var(--accent);
  }
  .address {
    position: absolute;
    right: 34px; top: 168px;
    text-align: right;
    font-size: 14px;
    line-height: 1.35;
    color: var(--ink);
  }
  .contacts {
    position: absolute;
    left: 34px; bottom: 26px;
    list-style: none;
    font-size: 15px;
    line-height: 1.45;
    color: var(--ink);
  }
  .contacts li { display: flex; align-items: center; gap: 9px; }
  .contacts svg { width: 14px; height: 14px; fill: var(--accent); flex: none; }
</style>
</head>
<body>

<section class="card card-front" aria-label="Card front">
  <div class="front-brand">
    <span class="brand-square"></span>
    <span class="brand-name">RIDGELINE</span>
  </div>
  <div class="front-brand-sub">DESIGN + BUILD</div>
  <div class="front-symbol-area" role="img" aria-label="Large dimensional brand symbol in green and black"></div>
</section>

<section class="card card-back" aria-label="Card back">
  <div class="back-brand">
    <span class="brand-square"></span>
    <span class="brand-name">RIDGELINE</span>
  </div>
  <div class="back-brand-sub">DESIGN + BUILD</div>

  <div class="person">
    <div class="person-name">Marcus Hale</div>
    <div class="person-title">Founder &amp; CEO</div>
  </div>

  <div class="rule"></div>

  <address class="address" style="font-style:normal">
    4471 Harbor Stone Pkwy<br>210-B, FL 32541
  </address>

  <ul class="contacts">
    <li>
      <svg viewBox="0 0 16 16" aria-hidden="true"><path d="M2 5c0-2 2-3 6-3s6 1 6 3v1h-3V5H5v1H2zM3 8h10l1 6H2z"/></svg>
      012-555-0148
    </li>
    <li>
      <svg viewBox="0 0 16 16" aria-hidden="true"><path d="M4 1l3 3-2 2c1 2 3 4 5 5l2-2 3 3-2 3C7 15 1 9 1 3z"/></svg>
      044-555-0192
    </li>
    <li>
      <svg viewBox="0 0 16 16" aria-hidden="true"><path d="M15 1L1 7l5 2 1 6 3-4 3 2z"/></svg>
      info@ridgelinebuild.com
    </li>
    <li>
      <svg viewBox="0 0 16 16" aria-hidden="true"><circle cx="8" cy="8" r="7"/><path d="M1 8h14M8 1c3 3 3 11 0 14M8 1c-3 3-3 11 0 14" stroke="#fff" stroke-width="1.2" fill="none"/></svg>
      www.ridgelinebuild.com
    </li>
  </ul>
</section>

</body>
</html>
```